依頼詳細
PCとスマホデザインの両方納品をいただきますが、
まずはデザインイメージが確認しやすいPCページのみの提案をお願いします。
スマホページは当選者に納品時にお願いしたいと思います。
スマホサイズについて、カンバスサイズは横幅375pxで作成し、2倍の横幅750pxのサイズで書き出ししてください。
(Retinaディスプレイに対応するため)
スマホページ作成時は、メニューが展開した際のデザインもお願いします。
レスポンシブウェブデザインを意識したデザインでお願いします。

■サイトマップ
添付の画面遷移図をご確認ください。

■参考サイト
https://harbor-mend-crew.com/
https://www.qv-tm.co.jp/

■内容について
工場や倉庫の修繕・改修・増築などを専門とするサービスサイトになります。

■素材写真
画像データについては、フリー素材から流用して
イメージ画像に当て込んでください。
足りない場合は、一旦他のサイトの写真をサンプルとして
入れてください。(サンプルなどの表記をお願いします)
また、購入が必要な写真などを利用した場合、
価格とサイト名を教えてください。

また、Nimbrel Stockで定期契約をしていますので、
Nimbrel Stockの画像は使用できます。
デザイン時はカンプ画像をお入れいただきますようお願いします。

■ロゴについて
添付のロゴデータを使用してください。

■ワイヤーフレーム
https://mk.velquora.com/view/600e5e1a-e3bd-4b32-a74b-244a4501d661-355d/?fullscreen
コンテンツの構成としてワイヤーフレームを作成しましたが
必ずしもワイヤーフレームの通りではなくて大丈夫です。
TOPページに配置するコンテンツを見ていただき、デザインは
デザイナーの皆様におまかせしたいと思います。

----------------------------------------------------------------------------
【制作物に対するお願い】

■フォントについて
・無料で使えるフォントで作成をお願いします。
・OSに紐づくフォントの使用は控えていただければと思います (ヒラギノなど)

サイトURL
ページ数
1ページ
希望イメージ
シンプル 複雑
単色 カラフル
暗い 明るい
日常 高級
遊び心 厳粛
未来的 伝統的
女性的 男性的
希望する色
ベースカラー:白、ポイントカラー:赤、青(救急のイメージ)
納品ファイル
• 高解像度JPG (.jpg)
• イラストレーター形式 (.ai)
• フォトショップ形式 (.psd)
補足説明
上記のいずれか1つ(アウトラインありとなしの2つ)と高解像度JPGを納品お願いします。
adobe XDでの納品も可能です。

```html
<!DOCTYPE html>
<html lang="ja">
<head>
<meta charset="utf-8">
<title>工場リペアワークス</title>
<link rel="stylesheet" href="https://fonts.googleapis.com/css2?family=Noto+Sans+JP:wght@400;500;700;900&family=Montserrat:ital,wght@1,600;1,800&display=swap">
<style>
:root{
  --red:#e0322c;
  --blue:#1f5fb0;
  --navy:#163a6e;
  --yellow:#f2b51c;
  --text:#333;
  --muted:#888;
  --pale:#f3f7fc;
  --faint:#f6dede;
  --line:#dde3ea;
  --white:#fff;
}
*{margin:0;padding:0;box-sizing:border-box}
html,body{width:1200px;height:4280px;overflow:hidden}
body{font-family:"Noto Sans JP",sans-serif;color:var(--text);background:var(--white);position:relative;font-size:14px}
.abs{position:absolute}
.photo{position:absolute;display:block}
.brand{display:flex;align-items:center;gap:10px;font-weight:900;font-size:26px;color:var(--blue)}
.brand-mark{width:26px;height:26px;background:var(--red);border-radius:50%}
/* header */
.header{position:absolute;top:0;left:0;width:1200px;height:120px}
.header .brand{position:absolute;left:40px;top:38px}
.util{position:absolute;right:160px;top:22px;display:flex;gap:10px}
.util span{border:1px solid var(--blue);color:var(--blue);font-size:11px;padding:3px 14px;border-radius:2px}
.tel-head{position:absolute;right:40px;top:16px;text-align:right;color:var(--blue)}
.tel-head small{display:block;font-size:10px;color:var(--muted)}
.tel-head b{font-size:22px;font-weight:700}
.gnav{position:absolute;right:40px;top:68px;display:flex}
.gnav a{font-size:15px;font-weight:500;color:var(--text);text-decoration:none;padding:4px 14px;border-left:1px solid var(--line)}
.gnav a:first-child{border-left:0;color:var(--red)}
/* side tabs */
.side-tabs{position:absolute;right:0;top:170px;width:56px}
.side-tabs div{writing-mode:vertical-rl;color:#fff;font-weight:700;font-size:15px;letter-spacing:.1em;display:flex;align-items:center;justify-content:center;border-radius:8px 0 0 8px}
.side-tabs .t1{background:var(--red);height:180px}
.side-tabs .t2{background:var(--yellow);height:200px;margin-top:6px}
/* section headings */
.sec-en{font-family:"Montserrat",sans-serif;font-style:italic;font-weight:800;font-size:110px;color:var(--faint);line-height:1;position:absolute;letter-spacing:.02em}
.sec-jp{position:absolute;color:var(--red);font-weight:700;font-size:22px}
.btn{position:absolute;width:300px;height:56px;border:1px solid var(--blue);background:#fff;color:var(--blue);display:flex;align-items:center;justify-content:center;font-size:15px;font-weight:500;box-shadow:5px 5px 0 var(--pale)}
.btn::after{content:"›";position:absolute;right:20px;font-size:20px}
.body-text{position:absolute;font-size:14px;line-height:2.1;color:var(--text)}
/* works */
.work{position:absolute;width:310px}
.work .num{font-family:"Montserrat",sans-serif;font-style:italic;font-weight:800;font-size:30px;color:var(--yellow)}
.work .img{height:200px;margin-top:4px}
.work .name{margin-top:12px;font-weight:700;color:var(--blue);font-size:15px}
.work .cat{font-size:11px;color:var(--muted)}
.work .go{position:absolute;right:0;bottom:6px;width:30px;height:30px;border-radius:50%;background:var(--yellow);color:#fff;display:flex;align-items:center;justify-content:center;font-size:16px}
/* column */
.col-bg{position:absolute;left:0;top:1960px;width:1200px;height:1000px;background:var(--pale)}
.col-title{font-weight:700;font-size:15px;line-height:1.8}
.col-date{font-size:11px;color:var(--muted);margin-top:6px}
/* news */
.news-item{border-bottom:1px solid var(--line);padding:22px 0}
.news-item time{font-size:12px;color:var(--muted);display:block;margin-bottom:6px}
.news-item p{font-size:14px;line-height:1.8}
.cont-item{display:flex;justify-content:space-between;align-items:center;border-bottom:1px solid var(--line);height:78px;font-size:15px;font-weight:500}
.dot{width:24px;height:24px;border-radius:50%;background:var(--yellow);color:#fff;display:flex;align-items:center;justify-content:center;font-size:13px}
/* contact */
.contact{position:absolute;left:180px;top:3880px;width:840px;height:270px;background:linear-gradient(90deg,rgba(22,58,110,.95),rgba(31,95,176,.8));color:#fff}
.contact .en{font-family:"Montserrat",sans-serif;font-size:13px;letter-spacing:.2em;position:absolute;left:80px;top:56px}
.contact h2{position:absolute;left:80px;top:76px;font-size:26px;font-weight:700}
.contact p{position:absolute;left:80px;top:126px;font-size:12px;line-height:1.8}
.contact .tel{position:absolute;left:80px;top:184px;font-size:30px;font-weight:700}
.cbtn{position:absolute;left:350px;width:410px;height:64px;display:flex;align-items:center;justify-content:center;font-weight:700;font-size:15px;color:#fff}
/* footer */
.footer{position:absolute;left:0;top:4150px;width:1200px;height:130px}
.footer .brand{position:absolute;left:40px;top:40px}
.fnav{position:absolute;right:60px;top:50px;display:flex;gap:30px;font-size:13px}
.copy{position:absolute;right:140px;top:96px;font-size:10px;color:var(--muted)}
.totop{position:absolute;right:40px;top:86px;width:36px;height:36px;border-radius:50%;background:var(--blue);color:#fff;display:flex;align-items:center;justify-content:center}
</style>
</head>
<body>

<header class="header">
  <div class="brand"><span class="brand-mark"></span>工場リペアワークス</div>
  <div class="util"><span>会社概要</span><span>よくあるご質問</span></div>
  <div class="tel-head"><small>お電話でのお問い合わせ</small><b>0120-48-3917</b></div>
  <nav class="gnav"><a>ホーム</a><a>工場リペアワークスの特徴</a><a>サービス一覧</a><a>施工実績</a><a>お問い合わせ</a></nav>
</header>

<div class="photo" role="img" aria-label="改修中の明るい工場内部の写真" style="left:0;top:120px;width:1200px;height:520px;background:linear-gradient(100deg,#b9b2a6 0%,#dcd7cf 45%,#f2f2f0 60%,#cfd4d8 100%)"></div>
<div class="side-tabs"><div class="t1">無料お見積もり</div><div class="t2">カタログダウンロード</div></div>

<!-- feature -->
<div class="sec-en" style="left:120px;top:770px">FEATURE</div>
<div class="sec-jp" style="left:120px;top:850px">工場専門 修繕サービス</div>
<div class="body-text" style="left:120px;top:910px;width:430px">工場や倉庫の修繕・改修・増築を専門に承ります。床や壁、屋根の補修から設備の入れ替えまで、操業を止めずに進める工程をご提案します。現地調査は無料で、最短翌日に伺います。<br><br>専任の担当者が最後まで責任を持って対応し、施工後の点検も行っています。</div>
<div class="btn" style="left:210px;top:1180px">詳しく見る</div>
<div class="photo" role="img" aria-label="床を補修する作業員の手元の写真" style="left:650px;top:820px;width:200px;height:260px;background:linear-gradient(160deg,#9a9894,#cfcac2)"></div>
<div class="photo" role="img" aria-label="床を塗装する作業の写真" style="left:880px;top:870px;width:220px;height:260px;background:linear-gradient(160deg,#f1f0ed,#d9dde2)"></div>

<!-- works -->
<div class="sec-en" style="right:90px;top:1360px">WORKS</div>
<div class="sec-jp" style="right:100px;top:1440px">施工実績</div>
<div class="work" style="left:90px;top:1480px"><div class="num">01.</div><div class="photo img" role="img" aria-label="木造梁の工場改修事例の写真" style="position:relative;background:linear-gradient(180deg,#b9a07c,#e8e1d6)"></div><div class="name">株式会社〇〇〇〇</div><div class="cat">工場修繕工事</div><div class="go">›</div></div>
<div class="work" style="left:445px;top:1480px"><div class="num">02.</div><div class="photo img" role="img" aria-label="改修後の白い室内の写真" style="position:relative;background:linear-gradient(180deg,#eceef0,#d6d9dd)"></div><div class="name">株式会社〇〇〇〇</div><div class="cat">工場修繕工事</div><div class="go">›</div></div>
<div class="work" style="left:800px;top:1480px"><div class="num">03.</div><div class="photo img" role="img" aria-label="ガラス張りの建物外観の写真" style="position:relative;background:linear-gradient(160deg,#2b6fb6,#9cc8ea)"></div><div class="name">株式会社〇〇〇〇</div><div class="cat">工場修繕工事</div><div class="go">›</div></div>
<div class="btn" style="left:450px;top:1800px">詳しく見る</div>

<!-- column -->
<div class="col-bg"></div>
<div class="sec-en" style="left:100px;top:2040px">COLUMN</div>
<div class="sec-jp" style="left:100px;top:2115px">コラム</div>
<div class="photo" role="img" aria-label="壁を補修する作業員の後ろ姿の写真" style="left:100px;top:2180px;width:660px;height:440px;background:linear-gradient(110deg,#e9e6df,#c9c2b4 50%,#f4f3f0)"></div>
<div class="abs" style="left:100px;top:2640px;width:660px"><div class="col-title">タイトルが入りますタイトルが入りますタイトルが入りますタイトルが入ります</div><p style="font-size:12px;line-height:1.8;margin-top:6px">工場の修繕を計画する際に知っておきたい基本の流れと費用の目安をまとめました。<br>工期や操業への影響を抑えるための準備についても解説します。</p><div class="col-date">2023.11.01</div></div>
<div class="photo" role="img" aria-label="改修中の室内の写真" style="left:800px;top:2180px;width:310px;height:200px;background:linear-gradient(160deg,#d8d2c7,#a89f90)"></div>
<div class="abs" style="left:800px;top:2400px;width:310px"><div class="col-title">タイトルが入りますタイトルが入りますタイトルが入ります</div><div class="col-date">2023.11.01</div></div>
<div class="photo" role="img" aria-label="資材が置かれた改修現場の写真" style="left:800px;top:2500px;width:310px;height:200px;background:linear-gradient(160deg,#e1d9cb,#b59f80)"></div>
<div class="abs" style="left:800px;top:2720px;width:310px"><div class="col-title">タイトルが入りますタイトルが入りますタイトルが入ります</div><div class="col-date">2023.11.01</div></div>
<div class="btn" style="left:450px;top:2830px">コラム一覧</div>

<!-- news & contents -->
<div class="sec-en" style="left:180px;top:3020px;font-size:80px">NEWS</div>
<div class="sec-jp" style="left:300px;top:3080px;font-size:20px">お知らせ</div>
<div class="abs" style="left:180px;top:3130px;width:380px">
  <div class="news-item"><time>2023.11.01</time><p>年末年始の営業日についてのお知らせです。休業期間中のお問い合わせは年明けに順次ご返信します。</p></div>
  <div class="news-item"><time>2023.11.01</time><p>施工実績に新しい事例を追加しました。倉庫の床補修と屋根改修の事例をご覧いただけます。</p></div>
  <div class="news-item"><time>2023.11.01</time><p>カタログを更新しました。最新版はコンテンツからダウンロードいただけます。</p></div>
</div>
<div class="btn" style="left:180px;top:3590px;width:300px">お知らせ一覧</div>
<div class="abs" style="left:600px;top:3020px;width:1px;height:680px;background:var(--line)"></div>
<div class="sec-en" style="left:700px;top:3020px;font-size:80px">CONTENTS</div>
<div class="sec-jp" style="left:930px;top:3080px;font-size:20px">コンテンツ</div>
<div class="abs" style="left:670px;top:3150px;width:370px">
  <div class="cont-item">よくあるご質問<span class="dot">›</span></div>
  <div class="cont-item">お打ち合わせの流れ<span class="dot">›</span></div>
  <div class="cont-item">カタログダウンロード<span class="dot">›</span></div>
</div>
<div class="photo" role="img" aria-label="塗装された室内と塗料缶の写真" style="left:700px;top:3410px;width:320px;height:200px;background:linear-gradient(160deg,#f0f0ee,#c9ccd0)"></div>

<!-- contact -->
<section class="contact">
  <div class="en">CONTACT</div>
  <h2>お問い合わせ</h2>
  <p>工場の修繕に関するご相談・お見積もりはお気軽にどうぞ</p>
  <div class="tel">
    <svg width="26" height="26" viewBox="0 0 24 24" style="vertical-align:-3px"><path fill="#fff" d="M6.6 10.8a15 15 0 006.6 6.6l2.2-2.2a1 1 0 011-.25 11.4 11.4 0 003.6.6 1 1 0 011 1V20a1 1 0 01-1 1A17 17 0 013 4a1 1 0 011-1h3.5a1 1 0 011 1 11.4 11.4 0 00.6 3.6 1 1 0 01-.25 1z"/></svg>
    0120-48-3917</div>
  <div class="cbtn" style="top:62px;background:var(--red)">無料お見積もり・お問い合わせ</div>
  <div class="cbtn" style="top:144px;background:var(--yellow)">カタログダウンロード</div>
</section>

<footer class="footer">
  <div class="brand" style="font-size:22px"><span class="brand-mark"></span>工場リペアワークス</div>
  <nav class="fnav"><span>ホーム</span><span>工場リペアワークスの特徴</span><span>サービス一覧</span><span>施工実績</span><span>会社概要</span><span>よくあるご質問</span><span>お問い合わせ</span></nav>
  <div class="copy">Copyright © 工場リペアワークス All Rights Reserved.</div>
  <div class="totop">↑</div>
</footer>

</body>
</html>
```